Velorin Biotechnology needs a professional powerpoint design

We would like to re-design our powerpoint template(as attachment 1), it should be based on our current logo (as attachment 2). We hope the new powerpoint template could be more professional and like a biotechnology company with advanced technology.
Velorin Biotechnology is a contract development and manufacturing organization to provide high quality services to our clients in development, lead-in advanced technology and cGMP manufacturing of biopharmaceuticals from clinical to commercial manufacturing. We offers the advanced technology and services to become the best partner for clients from clinical to commercial manufacturing.
Reason: We would like to extend the deadline for this project so that designers can have more time to prepare, thanks.
Target Market(s)
Velorin Biotechnology is a contract development and manufacturing organization to provide high quality services to our clients in development, lead-in advanced technology and cGMP manufacturing of biopharmaceuticals from clinical to commercial manufacturing.
Velorin primary focus on development and manufacturing of glycoprotein pharmaceuticals against breast cancer, supplies KEV Taiwan with KEV-347 & KEV-348 for global clinical trials and commercialization in the future. Velorin offers the advanced technology and services to become the best partner for clients from clinical to commercial manufacturing.
Industry/Entity Type
Biotechnology
Requirements
Must have
- The new powerpoint design should based on our current logo.
Should not have
- The similar design with current powerpoint style. Please don't refer the design style of our current website http://www.velorin-example.com.tw/ as well, we will re-design it soon.

```html
<!DOCTYPE html>
<html lang="en">
<head>
<meta charset="utf-8">
<title>Velorin Biotechnology – Presentation Template</title>
<link href="https://fonts.googleapis.com/css2?family=Open+Sans:wght@400;600;700&display=swap" rel="stylesheet">
<style>
:root{
  --ink:#0d2724;
  --deep:#133732;
  --teal:#1e4c45;
  --green:#78c167;
  --lime:#a8dc8a;
  --mist:#dfe9e4;
  --grey:#80898a;
  --text:#5b6362;
  --line:#cfd5d3;
  --paper:#ffffff;
  --sheet:#ffffff;
}
*{box-sizing:border-box;margin:0;padding:0}
html,body{width:1080px;height:1200px;overflow:hidden;background:var(--sheet)}
body{font-family:"Open Sans",Arial,sans-serif;color:var(--text)}
.sheet{width:1080px;height:1200px;padding:4px 8px;display:grid;grid-template-columns:repeat(3,344px);grid-template-rows:repeat(6,192px);gap:8px 16px}
.slide{position:relative;background:var(--paper);overflow:hidden;box-shadow:0 0 0 1px var(--line),0 1px 3px rgba(0,0,0,.18)}
.ph{position:absolute}
.foot{position:absolute;left:0;right:0;bottom:0;height:9px;background:var(--ink);color:#a9bcb7;font-size:4px;line-height:9px;padding-left:7px}
.foot .num{position:absolute;right:8px;top:2px;width:8px;height:5px;background:#fff;color:var(--ink);font-size:3.5px;line-height:5px;text-align:center}
.foot .date{position:absolute;right:8px;top:0}
.title{position:absolute;left:17px;top:13px;font-size:13px;font-weight:400;color:var(--ink);padding-bottom:3px;border-bottom:1px solid var(--line)}
.brand{position:absolute;right:10px;top:8px;display:flex;align-items:center;gap:3px}
.brand .dot{width:7px;height:7px;border-radius:50%;background:var(--green)}
.brand .name{font-size:8px;font-weight:700;line-height:7px;color:var(--ink);text-align:right}
.brand .name small{display:block;font-size:5px;line-height:6px}
.brand.light .name{color:#fff}
.small{font-size:4px;line-height:5.5px;color:var(--grey)}
.head{font-size:5px;font-weight:600;color:var(--ink)}
.ic{width:9px;height:9px;border-radius:50%;background:var(--ink);display:flex;align-items:center;justify-content:center;flex:none}
.ic svg{width:6px;height:6px}
.ic.sq{border-radius:1px}
.ic.light{background:#fff}
.lead{font-size:6px;color:var(--ink)}
.lead b{font-weight:700}
.para{font-size:4.2px;line-height:6px;color:var(--grey);margin-top:6px}

/* cover */
.cover .mark{position:absolute;left:92px;top:62px;display:flex;align-items:center;gap:8px}
.cover .mark .dot{width:22px;height:22px;border-radius:50%;background:var(--green)}
.cover .mark .name{color:#fff;font-weight:700;font-size:30px;line-height:30px;letter-spacing:1px}
.cover .mark .name small{display:block;text-align:right;font-size:16px;line-height:18px;letter-spacing:0}

/* title slides */
.hero-title{position:absolute;left:0;right:0;text-align:center;font-size:13px;color:#fff}
.hero-sub{position:absolute;left:0;right:0;text-align:center;font-size:4px;color:#b8cbc6}
.people{position:absolute;left:10px;right:10px;display:flex;gap:22px;align-items:center}
.person{display:flex;align-items:center;gap:4px}
.person .who{font-size:5px;font-weight:600;color:var(--ink);line-height:6px}
.person .who span{display:block;font-size:3.5px;font-weight:400;color:var(--grey)}
.logo-box{position:absolute;left:0;top:0;background:#fff;padding:7px 10px}
.logo-box .brand{position:static}

/* lists */
.agenda{position:absolute;left:36px;top:44px;display:grid;grid-template-columns:130px 130px;row-gap:16px;column-gap:10px}
.item{display:flex;gap:6px;align-items:flex-start}
.item .head{margin-bottom:1px}
.services{position:absolute;left:172px;top:38px;display:flex;flex-direction:column;gap:13px}
.stack{display:flex;flex-direction:column}

.panel{position:absolute;background:var(--ink);color:#fff}
.panel .head{color:#fff}
.panel .small{color:#9fb4af}
.quote{font-size:7px;line-height:10px;color:#fff}
.numdot{width:9px;height:9px;border-radius:50%;background:var(--ink);color:#fff;font-size:4.5px;line-height:9px;text-align:center;flex:none;font-weight:700}
.grid6{position:absolute;left:17px;top:40px;display:grid;grid-template-columns:repeat(3,100px);grid-template-rows:repeat(2,52px);gap:3px}
.grid6 .cell{position:relative;padding:6px 7px}
.grid6 .cell.dark{background:var(--ink)}
.grid6 .cell.mid{background:var(--grey)}
.grid6 .cell .head{color:#fff;margin-bottom:3px}
.grid6 .cell .small{color:#dfe6e4}
</style>
</head>
<body>
<svg width="0" height="0" style="position:absolute">
  <symbol id="i-clock" viewBox="0 0 10 10"><circle cx="5" cy="5" r="3.6" fill="none" stroke="#fff" stroke-width="1"/><path d="M5 3v2.2l1.5 1" fill="none" stroke="#fff" stroke-width="1"/></symbol>
  <symbol id="i-chart" viewBox="0 0 10 10"><path d="M2 8V6M4.5 8V4M7 8V2.5" stroke="#fff" stroke-width="1.4"/></symbol>
  <symbol id="i-arrow" viewBox="0 0 10 10"><path d="M2 8L8 2M4 2h4v4" fill="none" stroke="#fff" stroke-width="1.2"/></symbol>
  <symbol id="i-search" viewBox="0 0 10 10"><circle cx="4.3" cy="4.3" r="2.5" fill="none" stroke="#fff" stroke-width="1.1"/><path d="M6 6l2.3 2.3" stroke="#fff" stroke-width="1.2"/></symbol>
  <symbol id="i-pen" viewBox="0 0 10 10"><path d="M2 8l1-3 4-4 2 2-4 4z" fill="#fff"/></symbol>
  <symbol id="i-gear" viewBox="0 0 10 10"><circle cx="5" cy="5" r="2.2" fill="none" stroke="#fff" stroke-width="1.6" stroke-dasharray="1.2 .8"/><circle cx="5" cy="5" r="1" fill="#fff"/></symbol>
  <symbol id="i-user" viewBox="0 0 10 10"><circle cx="5" cy="3.4" r="1.8" fill="#fff"/><path d="M1.8 9c0-2 1.4-3.2 3.2-3.2S8.2 7 8.2 9z" fill="#fff"/></symbol>
  <symbol id="i-tick" viewBox="0 0 10 10"><path d="M2 5.2l2 2 4-4.4" fill="none" stroke="#fff" stroke-width="1.3"/></symbol>
</svg>

<main class="sheet">

  <!-- 1 cover -->
  <section class="slide cover" style="background:var(--ink)">
    <div class="ph" role="img" aria-label="Dark green background of glowing DNA strands" style="inset:0;background:radial-gradient(ellipse at 70% 80%,#2f5f52 0%,#173d36 40%,#0c2421 80%)"></div>
    <div class="mark"><span class="dot"></span><span class="name">Velorin<small>Biotech</small></span></div>
  </section>

  <!-- 2 title with photo -->
  <section class="slide">
    <div class="ph" role="img" aria-label="Scientist looking into a laboratory microscope" style="left:0;right:0;top:0;height:150px;background:linear-gradient(100deg,#c9d3cf 0%,#8e9e98 35%,#dfe5e2 70%,#b9c4bf 100%)"></div>
    <div class="logo-box"><div class="brand"><span class="dot"></span><span class="name">Velorin<small>Biotech</small></span></div></div>
    <div class="ph" style="left:0;right:0;top:104px;height:46px;background:rgba(22,68,58,.88)"></div>
    <div class="hero-title" style="top:113px">Your Title Goes Here</div>
    <div class="hero-sub" style="top:132px">Your Subtitle Goes Here</div>
    <div class="people" style="top:157px">
      <div class="person"><span class="ic"><svg><use href="#i-user"/></svg></span><span class="who">Mark Ellis<span>VP Marketing</span></span></div>
      <div class="person"><span class="ic"><svg><use href="#i-user"/></svg></span><span class="who">Anna Reyes<span>Senior Consultant</span></span></div>
      <div class="person"><span class="ic"><svg><use href="#i-user"/></svg></span><span class="who">Paul Grant<span>Vice President</span></span></div>
    </div>
    <div class="foot">© 2016 Velorin Biotech. All rights reserved.<span class="date">November 30, 2016</span></div>
  </section>

  <!-- 3 title with band -->
  <section class="slide">
    <div class="brand" style="left:10px;right:auto"><span class="dot"></span><span class="name">Velorin<small>Biotech</small></span></div>
    <div class="ph" role="img" aria-label="Green bacteria under the microscope" style="left:0;right:0;top:22px;height:94px;clip-path:polygon(0 28%,100% 0,100% 100%,0 100%);background:linear-gradient(90deg,#2c5a3c 0%,#7fbf6a 45%,#b7e39d 70%,#4f8a4d 100%)"></div>
    <div class="hero-title" style="top:120px;color:var(--ink)">Your Title Goes Here</div>
    <div class="hero-sub" style="top:138px;color:var(--grey)">Your Subtitle Goes Here</div>
    <div class="people" style="top:152px;left:8px;right:8px;border-top:1px solid var(--line);padding-top:5px;gap:14px">
      <div class="person"><span class="who">Mark Ellis<span>VP Marketing</span></span></div>
      <div class="person"><span class="who">Anna Reyes<span>Senior Consultant</span></span></div>
      <div class="person"><span class="who">Paul Grant<span>Vice President</span></span></div>
      <div class="small" style="margin-left:auto">Chemistry &amp; November 30, 2016</div>
    </div>
    <div class="ph" style="left:0;right:0;bottom:0;height:9px;background:var(--mist)"></div>
  </section>

  <!-- 4 agenda -->
  <section class="slide">
    <h2 class="title">Our Agenda</h2>
    <div class="brand"><span class="dot"></span><span class="name">Velorin<small>Biotech</small></span></div>
    <div class="agenda">
      <div class="item"><span class="ic sq"><svg><use href="#i-clock"/></svg></span><div><div class="head">Agenda One</div><div class="small">10:00<br>Short note on the first topic here</div></div></div>
      <div class="item"><span class="ic sq"><svg><use href="#i-clock"/></svg></span><div><div class="head">Agenda Four</div><div class="small">13:00<br>Short note on the fourth topic here</div></div></div>
      <div class="item"><span class="ic sq"><svg><use href="#i-clock"/></svg></span><div><div class="head">Agenda Two</div><div class="small">11:00<br>Short note on the second topic here</div></div></div>
      <div class="item"><span class="ic sq"><svg><use href="#i-clock"/></svg></span><div><div class="head">Agenda Five</div><div class="small">14:00<br>Short note on the fifth topic here</div></div></div>
      <div class="item"><span class="ic sq"><svg><use href="#i-clock"/></svg></span><div><div class="head">Agenda Three</div><div class="small">12:00<br>Short note on the third topic here</div></div></div>
      <div class="item"><span class="ic sq"><svg><use href="#i-clock"/></svg></span><div><div class="head">Agenda Six</div><div class="small">15:00<br>Short note on the sixth topic here</div></div></div>
    </div>
    <div class="foot">© 2016 Velorin Biotech. All rights reserved.<span class="num">2</span></div>
  </section>

  <!-- 5 services -->
  <section class="slide">
    <h2 class="title">Our Services</h2>
    <div class="brand"><span class="dot"></span><span class="name">Velorin<small>Biotech</small></span></div>
    <div class="ph" role="img" aria-label="Glowing green DNA double helix" style="left:17px;top:44px;width:133px;height:82px;background:linear-gradient(120deg,#0f2b24 0%,#3f7a4a 45%,#9bd37d 55%,#1d4a3a 100%)"></div>
    <div class="head" style="position:absolute;left:17px;top:132px">Your Title Goes Here</div>
    <div class="small" style="position:absolute;left:17px;top:140px;width:133px">Brief service summary text for this panel sits here in two or three lines</div>
    <div class="services">
      <div class="item"><span class="ic"><svg><use href="#i-chart"/></svg></span><div><div class="head">Service Number One</div><div class="small">Short line about this service<br>and what it offers clients</div></div></div>
      <div class="item"><span class="ic"><svg><use href="#i-arrow"/></svg></span><div><div class="head">Service Number Two</div><div class="small">Short line about this service<br>and what it offers clients</div></div></div>
      <div class="item"><span class="ic"><svg><use href="#i-search"/></svg></span><div><div class="head">Service Number One</div><div class="small">Short line about this service<br>and what it offers clients</div></div></div>
    </div>
    <div class="foot">© 2016 Velorin Biotech. All rights reserved.<span class="num">3</span></div>
  </section>

  <!-- 6 about -->
  <section class="slide">
    <div class="ph" role="img" aria-label="Colourful molecular structures in teal and orange light" style="left:0;top:0;width:270px;height:183px;background:radial-gradient(ellipse at 35% 45%,#d9a25a 0%,#5f7a58 25%,#23524d 55%,#0f2b29 100%)"></div>
    <div class="brand"><span class="dot"></span><span class="name">Velorin<small>Biotech</small></span></div>
    <div class="panel" style="left:170px;top:40px;width:174px;height:96px;padding:12px 14px">
      <div style="font-size:12px">About Us</div>
      <div class="small" style="margin-top:6px;color:#c9d6d3">Short intro about the company and its work sits here across a few lines of text.</div>
      <div class="small" style="margin-top:6px;color:#c9d6d3">A second line of text adds more detail about the team and its goals.</div>
    </div>
    <div class="foot">© 2016 Velorin Biotech. All rights reserved.<span class="num">4</span></div>
  </section>

  <!-- 7 quote area -->
  <section class="slide">
    <h2 class="title">Quote Area</h2>
    <div class="brand"><span class="dot"></span><span class="name">Velorin<small>Biotech</small></span></div>
    <div class="panel" style="left:0;right:0;top:40px;height:96px"></div>
    <div class="ph" role="img" aria-label="Green bacteria close up" style="left:150px;right:0;top:40px;height:96px;background:linear-gradient(90deg,#1b3d2c 0%,#6faa5a 40%,#b9e19c 65%,#5c9550 100%)"></div>
    <div class="quote" style="position:absolute;left:14px;top:64px;width:140px">“ Coming together is a beginning.<br>Keeping together is progress.<br>Working together is success. ”</div>
    <div class="small" style="position:absolute;left:20px;top:104px;color:#b9cac6">- Walter Hale -</div>
    <div class="foot">© 2016 Velorin Biotech. All rights reserved.<span class="num">5</span></div>
  </section>

  <!-- 8 text area -->
  <section class="slide">
    <h2 class="title">Text Area</h2>
    <div class="brand"><span class="dot"></span><span class="name">Velorin<small>Biotech</small></span></div>
    <div style="position:absolute;left:20px;top:58px;width:305px">
      <div class="lead">We are <b>Velorin</b> Biotech</div>
      <div class="para">Our team develops and manufactures complex biologic medicines for partners worldwide, from early clinical work to full commercial supply with strict quality control at each step.</div>
      <div class="para">We combine process design, analytics and cGMP production under one roof, so each project moves quickly and safely from the lab bench to patients who need it.</div>
      <div class="para">We welcome new partners and look forward to building lasting work together.</div>
    </div>
    <div class="foot">© 2016 Velorin Biotech. All rights reserved.<span class="num">6</span></div>
  </section>

  <!-- 9 vision & mission -->
  <section class="slide">
    <h2 class="title">Our Vision &amp; Mission</h2>
    <div class="brand"><span class="dot"></span><span class="name">Velorin<small>Biotech</small></span></div>
    <div class="panel" style="left:0;right:0;top:40px;height:102px;background:linear-gradient(90deg,#0d2724 0%,#173c36 70%,#24524a 100%)"></div>
    <div style="position:absolute;left:16px;top:50px;width:130px;color:#fff">
      <div style="font-size:7px">• Our Vision:</div>
      <div style="font-size:6px;font-weight:600;margin:2px 0 0 7px;line-height:8px">Go to the Next Level<br>Without look in the past</div>
      <div class="small" style="margin:6px 0 0 7px;color:#a9bdb8">Short vision text describing where the company is heading in the years ahead.</div>
    </div>
    <div style="position:absolute;left:180px;top:50px;width:150px;color:#fff">
      <div style="font-size:7px">• Our Missions:</div>
      <div class="stack" style="gap:6px;margin-top:5px">
        <div class="item"><span class="ic light" style="background:#e7ecea"></span><div><div class="head" style="color:#fff">Your Text Here</div><div class="small" style="color:#a9bdb8">Short mission line goes here</div></div></div>
        <div class="item"><span class="ic light" style="background:#e7ecea"></span><div><div class="head" style="color:#fff">Your Text Here</div><div class="small" style="color:#a9bdb8">Short mission line goes here</div></div></div>
        <div class="item"><span class="ic light" style="background:#e7ecea"></span><div><div class="head" style="color:#fff">Your Text Here</div><div class="small" style="color:#a9bdb8">Short mission line goes here</div></div></div>
      </div>
    </div>
    <div class="foot">© 2016 Velorin Biotech. All rights reserved.<span class="num">7</span></div>
  </section>

  <!-- 10 full quote -->
  <section class="slide" style="background:var(--ink)">
    <div class="ph" role="img" aria-label="Dark green DNA helix background" style="inset:0;background:radial-gradient(ellipse at 25% 30%,#5f9a5a 0%,#234a3a 35%,#0f2a25 70%),#0f2a25"></div>
    <div style="position:absolute;left:160px;top:42px;width:24px;height:24px;border-radius:50%;background:#8b9896;color:#fff;font-size:16px;line-height:28px;text-align:center;font-weight:700">“</div>
    <div class="quote" style="position:absolute;left:0;right:0;top:74px;text-align:center;font-size:8px;line-height:11px">Coming together is a beginning.<br>Keeping together is progress.<br>Working together is success.</div>
    <div class="small" style="position:absolute;left:0;right:0;top:116px;text-align:center;color:#b5c6c2">Walter Hale</div>
  </section>

  <!-- 11 text area card -->
  <section class="slide">
    <div class="ph" style="left:0;top:0;width:170px;height:183px;background:var(--ink)"></div>
    <div class="ph" style="left:170px;top:0;right:0;height:183px;background:#8a9190"></div>
    <div class="ph" style="left:12px;top:12px;width:318px;height:146px;background:#fff"></div>
    <h2 class="title" style="left:24px;top:22px">Text Area</h2>
    <div class="brand" style="right:22px;top:20px"><span class="dot"></span><span class="name">Velorin<small>Biotech</small></span></div>
    <div style="position:absolute;left:24px;top:56px;width:296px">
      <div class="lead">We are <b>Velorin</b> Biotech</div>
      <div class="para">Our team develops and manufactures complex biologic medicines for partners worldwide, from early clinical work to full commercial supply.</div>
      <div class="para">We combine process design, analytics and cGMP production under one roof, so each project moves quickly from lab to patient.</div>
      <div class="para">New partners are always welcome to talk with our team about their next program.</div>
    </div>
  </section>

  <!-- 12 logo photo + numbered -->
  <section class="slide">
    <div class="ph" role="img" aria-label="Green DNA strands on a dark background" style="left:0;top:0;width:170px;height:155px;background:linear-gradient(135deg,#8fc97a 0%,#3f7a4f 35%,#173b33 70%,#0d2724 100%)"></div>
    <div class="brand light" style="left:40px;right:auto;top:66px"><span class="dot" style="width:12px;height:12px"></span><span class="name" style="font-size:14px;line-height:13px">Velorin<small style="font-size:8px;line-height:10px">Biotech</small></span></div>
    <div class="brand"><span class="dot"></span><span class="name">Velorin<small>Biotech</small></span></div>
    <div style="position:absolute;left:182px;top:46px;font-size:11px;color:var(--ink)">Your Title Goes Here</div>
    <div class="stack" style="position:absolute;left:182px;top:70px;gap:12px;width:150px">
      <div class="item"><span class="numdot">1</span><div><div class="head">Your Text Goes Here</div><div class="small">Short supporting line of text<br>sits in this spot</div></div></div>
      <div class="item"><span class="numdot">2</span><div><div class="head">Your Text Goes Here</div><div class="small">Short supporting line of text<br>sits in this spot</div></div></div>
    </div>
    <div class="foot">© 2016 Velorin Biotech. All rights reserved.<span class="num">10</span></div>
  </section>

  <!-- 13 six grid -->
  <section class="slide">
    <h2 class="title">Your Title Goes Here</h2>
    <div class="brand"><span class="dot"></span><span class="name">Velorin<small>Biotech</small></span></div>
    <div class="grid6">
      <div class="cell" role="img" aria-label="Green virus particle" style="background:radial-gradient(circle at 40% 50%,#b5e09a 0%,#5e9a4f 40%,#1d3d2c 100%)"></div>
      <div class="cell mid"><div class="head">Heading Goes Here</div><div class="small">Short text for this tile<br>goes here in a few lines</div></div>
      <div class="cell" role="img" aria-label="Green bacteria strands" style="background:linear-gradient(120deg,#cdeab6 0%,#8cc46f 50%,#4a7d43 100%)"></div>
      <div class="cell dark"><div class="head">Heading Goes Here</div><div class="small">Short text for this tile<br>goes here in a few lines</div></div>
      <div class="cell" role="img" aria-label="Green virus on black" style="background:radial-gradient(circle at 50% 50%,#7fbf68 0%,#2f5a32 35%,#070d0a 70%)"></div>
      <div class="cell dark"><div class="head">Heading Goes Here</div><div class="small">Short text for this tile<br>goes here in a few lines</div></div>
    </div>
    <div class="foot">© 2016 Velorin Biotech. All rights reserved.<span class="num">11</span></div>
  </section>

  <!-- 14 lab collage -->
  <section class="slide">
    <div class="ph" style="left:0;top:0;width:112px;height:72px;background:var(--ink)"></div>
    <div class="brand light" style="left:14px;right:auto;top:24px"><span class="dot" style="width:11px;height:11px"></span><span class="name" style="font-size:13px;line-height:12px">Velorin<small style="font-size:7px;line-height:9px">Biotech</small></span></div>
    <div class="ph" role="img" aria-label="Researcher in mask and gloves holding a flask of red liquid" style="left:114px;top:0;width:75px;height:105px;background:linear-gradient(160deg,#eef1f2 0%,#c9d2d6 45%,#e8ecec 60%,#b8c8d6 100%)"></div>
    <div class="ph" role="img" aria-label="Scientist working at a microscope" style="left:0;top:74px;width:112px;height:109px;background:linear-gradient(120deg,#c7ccd0 0%,#7d8a90 45%,#e2e6e8 100%)"></div>
    <div class="ph" role="img" aria-label="Laboratory bench detail" style="left:114px;top:107px;width:75px;height:76px;background:linear-gradient(180deg,#dbe1e4,#aab5bb)"></div>
    <div class="brand"><span class="dot"></span><span class="name">Velorin<small>Biotech</small></span></div>
    <div style="position:absolute;left:198px;top:42px;font-size:11px;line-height:13px;color:var(--ink)">Your Title<br>Goes Here</div>
    <div class="small" style="position:absolute;left:198px;top:72px;width:135px">Short paragraph of body text about this lab area sits here.</div>
    <div class="small" style="position:absolute;left:198px;top:94px;width:135px">Second paragraph adds more detail on the work done here.</div>
    <div class="small" style="position:absolute;left:198px;top:116px;width:135px">A third short block closes the text column on this page.</div>
    <div class="foot">© 2016 Velorin Biotech. All rights reserved.<span class="num">12</span></div>
  </section>

  <!-- 15 text + strips -->
  <section class="slide">
    <h2 class="title">Your Title Goes Here</h2>
    <div class="brand"><span class="dot"></span><span class="name">Velorin<small>Biotech</small></span></div>
    <div style="position:absolute;left:20px;top:60px;width:130px">
      <div class="lead">We are <b>Velorin</b> Biotech</div>
      <div class="para">Short paragraph about our lab teams and the quality systems that guide every batch we make.</div>
      <div class="para">A second short block adds a few more words on our services.</div>
    </div>
    <div class="ph" role="img" aria-label="Microscope lens close up" style="left:168px;top:48px;width:52px;height:95px;background:linear-gradient(180deg,#8a9599,#dfe3e4 60%,#a9b2b5)"></div>
    <div class="ph" role="img" aria-label="Scientist at a microscope" style="left:223px;top:48px;width:52px;height:95px;background:linear-gradient(180deg,#c9cfd1,#7f8b8e 50%,#e4e7e8)"></div>
    <div class="ph" role="img" aria-label="Laboratory microscope" style="left:278px;top:48px;width:52px;height:95px;background:linear-gradient(180deg,#e8ebec,#a7b0b3 55%,#d5dadb)"></div>
    <div class="foot">© 2016 Velorin Biotech. All rights reserved.<span class="num">13</span></div>
  </section>

  <!-- 16 differences -->
  <section class="slide">
    <h2 class="title">Our Differences</h2>
    <div class="brand"><span class="dot"></span><span class="name">Velorin<small>Biotech</small></span></div>
    <div class="panel" style="left:24px;right:18px;top:44px;height:104px"></div>
    <div class="stack" style="position:absolute;left:36px;top:52px;gap:9px;width:138px">
      <div class="item" style="align-items:center"><span class="ic light"><svg><use href="#i-tick" style="color:#000"/></svg></span><div class="small" style="color:#c4d2ce">Short point on what sets our work apart.</div></div>
      <div class="item" style="align-items:center"><span class="ic light"><svg><use href="#i-pen"/></svg></span><div class="small" style="color:#c4d2ce">Short point on what sets our work apart.</div></div>
      <div class="item" style="align-items:center"><span class="ic light"><svg><use href="#i-gear"/></svg></span><div class="small" style="color:#c4d2ce">Short point on what sets our work apart.</div></div>
      <div class="item" style="align-items:center"><span class="ic light"><svg><use href="#i-search"/></svg></span><div class="small" style="color:#c4d2ce">Short point on what sets our work apart.</div></div>
    </div>
    <div class="ph" role="img" aria-label="Researchers working at computer screens in a lab" style="left:196px;top:56px;width:120px;height:80px;background:linear-gradient(120deg,#566066 0%,#9aa5aa 45%,#3d474c 100%)"></div>
    <div class="foot">© 2016 Velorin Biotech. All rights reserved.<span class="num">14</span></div>
  </section>

  <!-- 17 portfolio -->
  <section class="slide">
    <h2 class="title">Portfolio Area</h2>
    <div class="head" style="position:absolute;left:17px;top:38px">Heading Goes Here</div>
    <div class="small" style="position:absolute;left:17px;top:45px;width:130px">Short intro line for the portfolio items listed below.</div>
    <div class="stack" style="position:absolute;left:17px;top:62px;gap:6px">
      <div class="item"><span class="ic"><svg><use href="#i-search"/></svg></span><div><div class="head">Your Text Here</div><div class="small">Short detail line here</div></div></div>
      <div class="item"><span class="ic"><svg><use href="#i-pen"/></svg></span><div><div class="head">Your Text Here</div><div class="small">Short detail line here</div></div></div>
      <div class="item"><span class="ic"><svg><use href="#i-arrow"/></svg></span><div><div class="head">Your Text Here</div><div class="small">Short detail line here</div></div></div>
      <div class="item"><span class="ic"><svg><use href="#i-gear"/></svg></span><div><div class="head">Your Text Here</div><div class="small">Short detail line here</div></div></div>
    </div>
    <div class="ph" role="img" aria-label="Lab worker in protective mask" style="left:160px;top:0;width:90px;height:91px;background:linear-gradient(160deg,#e9dfd6,#c9c2bc 60%,#f1eeeb)"></div>
    <div class="ph" role="img" aria-label="Lab worker in white coat" style="left:252px;top:0;width:92px;height:91px;background:linear-gradient(160deg,#eef0f1,#cdd3d6)"></div>
    <div class="ph" role="img" aria-label="Gloved hand holding a petri dish" style="left:160px;top:93px;width:90px;height:90px;background:linear-gradient(200deg,#e5e9ec,#8eb0d6 70%,#d2dbe3)"></div>
    <div class="ph" role="img" aria-label="Blue gloves handling samples" style="left:252px;top:93px;width:92px;height:90px;background:linear-gradient(200deg,#f0f2f3,#7aa6d8 65%,#e1e6ea)"></div>
    <div class="foot">© 2016 Velorin Biotech. All rights reserved.<span class="num">15</span></div>
  </section>

  <!-- 18 headings list -->
  <section class="slide">
    <div class="brand" style="left:17px;right:auto;top:12px"><span class="dot"></span><span class="name">Velorin<small>Biotech</small></span></div>
    <h2 class="title" style="top:38px">Your Title Goes Here</h2>
    <div class="stack" style="position:absolute;left:28px;top:68px;gap:9px;width:150px">
      <div class="item"><span class="ic"><svg><use href="#i-chart"/></svg></span><div><div class="head">Heading One</div><div class="small">Short line of body text here<br>on this first topic</div></div></div>
      <div class="item"><span class="ic"><svg><use href="#i-arrow"/></svg></span><div><div class="head">Heading Two</div><div class="small">Short line of body text here<br>on this second topic</div></div></div>
      <div class="item"><span class="ic"><svg><use href="#i-search"/></svg></span><div><div class="head">Heading Three</div><div class="small">Short line of body text here<br>on this third topic</div></div></div>
    </div>
    <div class="ph" role="img" aria-label="Scientist using a pipette over blue test tubes" style="left:200px;top:0;right:0;height:183px;background:linear-gradient(180deg,#f3f1ee 0%,#d9d4cf 35%,#eef1f3 60%,#9cc2e6 85%,#e9eef2 100%)"></div>
    <div class="foot">© 2016 Velorin Biotech. All rights reserved.<span class="num">16</span></div>
  </section>

</main>
</body>
</html>
```